harborKettrix.com Blog/website

This is new site, we do not have any current content
Would like a website for harbor kettrix. The site will cover what to expect getting started, what to wear. How to pick out a kettrix Gym (called a box).
We will be posting articles on exercises and how to properly perform and occasional product review.
We would like a section on recipes and what to eat and not to eat
We are attempting to remove the barrier of entry to get new people transform their lives/body and try kettrix.
Will also like to post daily Work outs which are called WODs (workout of the day) and exercises.
The sections of the site I envision are
• the front landing page
• Contact Page
• Blog Page
• About Page
• Recipe Page
• Exercise Page
• FAQ and frequently used Terms

Target Market(s)

Fitness market, people interested or just starting kettrix

Industry/Entity Type

Fitness

Logo Text

harbor Kettrix - your kettrix start page - or something like that

Coding

Coded - Design and coding required

Number of Pages Required

5+ page

Font styles to use
Sans Serif

Requirements
Must have
• Frontpage, Contact Page, Blog Page, about page and FAQ and Terms Page
• This will be on a wordpress site
Nice to have
• would like to have more of a female slant and feel. photos of workouts

```html
<!DOCTYPE html>
<html lang="en">
<head>
<meta charset="utf-8">
<title>Harbor Kettrix</title>
<link href="https://fonts.googleapis.com/css2?family=Montserrat:wght@400;500;600;700&family=Open+Sans:wght@400;600&display=swap" rel="stylesheet">
<style>
:root{
  --ink:#1f2124;
  --panel:#25272a;
  --deep:#141516;
  --light:#f2f2f2;
  --white:#ffffff;
  --muted:#8a8d91;
  --soft:#c9cbce;
  --line:#dcdcdc;
}
*{box-sizing:border-box;margin:0;padding:0}
html,body{width:1200px;height:2560px;overflow:hidden}
body{background:var(--light);font-family:"Open Sans",Arial,sans-serif;color:var(--ink);position:relative}
.head{font-family:"Montserrat",Arial,sans-serif}

/* header + hero */
.hero{position:absolute;left:0;top:0;width:1200px;height:600px;background:radial-gradient(ellipse at 50% 40%,#5a5b5d 0%,#2c2d2f 45%,#141516 100%)}
.topbar{position:absolute;left:0;top:0;width:1200px;height:64px;display:flex;align-items:center;justify-content:space-between;padding:0 240px;border-bottom:1px solid rgba(255,255,255,.12)}
.brand{display:flex;align-items:center;gap:10px;color:var(--white);font:700 17px "Montserrat",Arial,sans-serif;letter-spacing:1px}
.brand-dot{width:24px;height:24px;border:2px solid var(--white);border-radius:50%}
.nav{display:flex;gap:22px;align-items:center;color:var(--white);font:600 10px "Montserrat",Arial,sans-serif;letter-spacing:1px}
.hero-title{position:absolute;left:0;width:1200px;top:250px;text-align:center;color:var(--white);font:600 30px "Montserrat",Arial,sans-serif;letter-spacing:.5px}
.hero-sub{position:absolute;left:0;width:1200px;top:300px;text-align:center;color:var(--soft);font-size:12px}
.btn{display:inline-block;border:2px solid var(--white);color:var(--white);font:600 11px "Montserrat",Arial,sans-serif;letter-spacing:1px;padding:10px 22px}
.btn-dark{border-color:#9a9a9a;color:var(--ink)}
.hero-btn{position:absolute;left:540px;top:330px}

/* news */
.section-title{text-align:center;font:500 18px "Montserrat",Arial,sans-serif;letter-spacing:2px;color:#555}
.news{position:absolute;left:0;top:600px;width:1200px;height:580px;background:var(--light)}
.news .section-title{position:absolute;top:70px;width:1200px}
.cards{position:absolute;left:250px;top:150px;display:flex;gap:30px}
.card{width:213px}
.card-photo{height:115px;background:linear-gradient(135deg,#6f7173,#2a2b2d)}
.card-body{display:flex;gap:10px;padding-top:12px}
.date{width:34px;height:40px;background:var(--ink);color:var(--white);font:700 14px "Montserrat",sans-serif;text-align:center;padding-top:5px;line-height:1}
.date small{display:block;font-size:8px;font-weight:500;margin-top:3px}
.card-title{font:600 10px "Montserrat",sans-serif;line-height:1.4;text-transform:uppercase;color:#333}
.meta{margin-top:10px;font-size:9px;color:var(--muted);display:flex;gap:12px}
.news-btn{position:absolute;left:542px;top:460px}

/* about / exercise */
.photo{position:absolute;role:img}
.about-photo{left:0;top:1180px;width:600px;height:300px;background:linear-gradient(120deg,#3a3b3d,#7b7c7e 50%,#2d2e30)}
.about-panel{position:absolute;left:600px;top:1180px;width:600px;height:300px;background:var(--panel);color:var(--white);padding:40px 40px}
.ex-panel{position:absolute;left:0;top:1480px;width:600px;height:300px;background:var(--panel);color:var(--white);padding:40px 40px;text-align:right}
.ex-photo{left:600px;top:1480px;width:600px;height:300px;background:linear-gradient(200deg,#8a8b8d,#3a3b3d 60%,#1f2022)}
.panel-title{font:600 15px "Montserrat",sans-serif;letter-spacing:1px;margin-bottom:16px}
.panel-text{font-size:11px;line-height:1.7;color:var(--soft);max-width:330px}
.ex-panel .panel-text{margin-left:auto}
.panel-btn{margin-top:22px}

/* video strip */
.strip{left:0;top:1780px;width:1200px;height:260px;background:linear-gradient(90deg,#3c3d3f,#6d6e70 40%,#2a2b2d 75%,#454648)}
.play{position:absolute;left:574px;top:1884px;width:52px;height:52px;border-radius:50%;background:var(--white)}

/* contact */
.contact{position:absolute;left:0;top:2040px;width:1200px;height:420px;background:var(--light)}
.contact-title{position:absolute;left:250px;top:60px;font:600 15px "Montserrat",sans-serif;letter-spacing:1px;color:#444}
.form{position:absolute;left:250px;top:110px;width:330px}
.field{height:34px;border-bottom:1px solid var(--line);font-size:10px;color:var(--muted);padding-top:12px}
.field.tall{height:70px}
.form .btn{margin-top:24px;padding:8px 22px;font-size:10px}
.info{position:absolute;left:760px;top:110px;width:200px}
.info-row{display:flex;gap:14px;margin-bottom:26px}
.info-row svg{flex:none}
.info-label{font:600 10px "Montserrat",sans-serif;color:#555}
.info-val{font-size:10px;color:var(--muted);margin-top:4px;line-height:1.5}
.social{display:flex;gap:8px;align-items:center;font-size:10px;color:var(--muted)}
.social span.c{width:22px;height:22px;border:1px solid #aaa;border-radius:50%}

/* footer */
.footer{position:absolute;left:0;top:2460px;width:1200px;height:100px;background:var(--deep);color:var(--muted);font-size:10px;display:flex;align-items:center;justify-content:space-between;padding:0 60px}
.footer nav{display:flex;gap:22px;font:500 10px "Montserrat",sans-serif;letter-spacing:1px}
.totop{width:26px;height:26px;border-radius:50%;border:1px solid #555}
</style>
</head>
<body>

<header class="hero" role="img" aria-label="Athlete lifting a barbell overhead in a dark gym">
  <div class="topbar">
    <div class="brand"><span class="brand-dot"></span>HARBOR KETTRIX</div>
    <nav class="nav">
      <span>HOME</span><span>BLOG</span><span>ABOUT US</span><span>EXERCISE</span><span>RECIPES</span><span>FAQ</span>
      <svg width="12" height="12" viewBox="0 0 12 12"><circle cx="5" cy="5" r="4" fill="none" stroke="#fff" stroke-width="1.5"/><line x1="8" y1="8" x2="11.5" y2="11.5" stroke="#fff" stroke-width="1.5"/></svg>
    </nav>
  </div>
  <h1 class="hero-title">THE WORLD'S LARGEST OLYMPIC WEIGHTLIFTING EDUCATION SOURCE</h1>
  <p class="hero-sub">Start strong, train smart</p>
  <span class="btn hero-btn">LEARN MORE</span>
</header>

<section class="news">
  <h2 class="section-title">LATEST NEWS</h2>
  <div class="cards">
    <article class="card">
      <div class="card-photo" role="img" aria-label="Woman training with a barbell"></div>
      <div class="card-body"><div class="date">23<small>JAN</small></div><div><h3 class="card-title">What to wear for your first box session</h3><div class="meta"><span>Admin</span><span>12 likes</span><span>4 notes</span></div></div></div>
    </article>
    <article class="card">
      <div class="card-photo" role="img" aria-label="Athlete performing a deadlift"></div>
      <div class="card-body"><div class="date">23<small>JAN</small></div><div><h3 class="card-title">How to pick the right kettrix box near you</h3><div class="meta"><span>Admin</span><span>9 likes</span><span>2 notes</span></div></div></div>
    </article>
    <article class="card">
      <div class="card-photo" role="img" aria-label="Lifter preparing at the barbell"></div>
      <div class="card-body"><div class="date">23<small>JAN</small></div><div><h3 class="card-title">Today's WOD and proper squat form tips</h3><div class="meta"><span>Admin</span><span>15 likes</span><span>6 notes</span></div></div></div>
    </article>
  </div>
  <span class="btn btn-dark news-btn">ALL NEWS</span>
</section>

<div class="photo about-photo" role="img" aria-label="Women lifting barbells in a gym"></div>
<section class="about-panel">
  <h2 class="panel-title">ABOUT US</h2>
  <p class="panel-text">Harbor Kettrix is your start page for strength training. We explain what to expect on day one, how to choose a box, what to wear and how to move safely, so every beginner can begin with confidence and build lasting habits at their own pace.</p>
  <span class="btn panel-btn">LEARN MORE</span>
</section>

<section class="ex-panel">
  <h2 class="panel-title">EXERCISE</h2>
  <p class="panel-text">Step by step guides for every core movement, from the air squat to the clean and jerk. Each article covers setup, common faults and scaling options, plus the daily WOD to put it all into practice with your coach and friends.</p>
  <span class="btn panel-btn">LEARN MORE</span>
</section>
<div class="photo ex-photo" role="img" aria-label="Athlete resting between sets in a gym"></div>

<div class="photo strip" role="img" aria-label="Athletes training together, workout video preview"></div>
<svg class="play" viewBox="0 0 52 52" role="img" aria-label="Play video"><circle cx="26" cy="26" r="26" fill="#fff"/><path d="M21 17 L35 26 L21 35 Z" fill="#1f2124"/></svg>

<section class="contact">
  <h2 class="contact-title">CONTACT US</h2>
  <form class="form">
    <div class="field">Name</div>
    <div class="field">Email</div>
    <div class="field">Subject</div>
    <div class="field tall">Message</div>
    <span class="btn btn-dark">SEND</span>
  </form>
  <div class="info">
    <div class="info-row">
      <svg width="14" height="16" viewBox="0 0 14 16"><path d="M7 1a5 5 0 0 0-5 5c0 4 5 9 5 9s5-5 5-9a5 5 0 0 0-5-5z" fill="none" stroke="#888"/><circle cx="7" cy="6" r="1.8" fill="#888"/></svg>
      <div><div class="info-label">Address</div><div class="info-val">42 Quayside Lane, Portmere</div></div>
    </div>
    <div class="info-row">
      <svg width="14" height="14" viewBox="0 0 14 14"><rect x="1" y="3" width="12" height="8" fill="none" stroke="#888"/><path d="M1 3l6 5 6-5" fill="none" stroke="#888"/></svg>
      <div><div class="info-label">Email</div><div class="info-val">hello@harborkettrix.com</div></div>
    </div>
    <div class="info-row">
      <svg width="14" height="14" viewBox="0 0 14 14"><path d="M3 1l3 3-2 2a8 8 0 0 0 4 4l2-2 3 3-2 2C6 13 1 8 1 3z" fill="none" stroke="#888"/></svg>
      <div><div class="info-label">Phone</div><div class="info-val">+1 555 0148</div></div>
    </div>
    <div class="social">Follow us <span class="c"></span><span class="c"></span><span class="c"></span></div>
  </div>
</section>

<footer class="footer">
  <span>© 2024 Harbor Kettrix. All rights reserved.</span>
  <nav><span>HOME</span><span>BLOG</span><span>ABOUT</span><span>RECIPES</span><span>FAQ</span><span>CONTACT</span></nav>
  <span class="totop"></span>
</footer>

</body>
</html>
```